Business Card Design

We do Metal Roofing, fascia and gutter and edge protection [safety rail].

Industry/Entity Type

Business

Contact Information for Business Card

Tarnwell Roof Plumbing. Metal Roofing, Fascia and Gutter, Edge Protection
Colin 0468305172
Finn 0419587364
tr7win5@mailvane.com
Lic: 614903K
ABN:52716340951

```html
<!DOCTYPE html>
<html lang="en">
<head>
<meta charset="utf-8">
<title>Tarnwell Roof Plumbing – Business Card</title>
<link rel="stylesheet" href="https://fonts.googleapis.com/css2?family=Montserrat:wght@400;700&display=swap">
<style>
  :root {
    --brand-blue: #0f52a0;
    --brand-grey: #9aa5b1;
    --text-grey: #8c96a0;
    --card-white: #ffffff;
    --backdrop: #e9e7e4;
  }
  html, body {
    margin: 0;
    padding: 0;
    width: 1200px;
    height: 1000px;
    overflow: hidden;
    background: var(--backdrop);
    font-family: "Montserrat", Arial, sans-serif;
  }
  .canvas { position: relative; width: 1200px; height: 1000px; }
  .card {
    position: absolute;
    left: 265px;
    width: 665px;
    height: 397px;
    box-shadow: 0 4px 14px rgba(0,0,0,0.18);
    overflow: hidden;
  }
  .card--front { top: 73px; background: var(--brand-blue); }
  .card--back { top: 533px; background: var(--card-white); }

  .wordmark {
    position: absolute;
    font-weight: 700;
    text-transform: uppercase;
    letter-spacing: 0.5px;
    text-align: center;
    line-height: 1.12;
    margin: 0;
  }
  .card--front .wordmark {
    left: 0; right: 0; top: 140px;
    font-size: 40px;
    color: var(--card-white);
  }
  .card--back .wordmark {
    left: 330px; width: 300px; top: 85px;
    font-size: 30px;
    color: var(--brand-blue);
  }

  .contacts { position: absolute; left: 39px; top: 74px; }
  .person__name {
    font-size: 20px; font-weight: 700; color: var(--brand-blue);
    margin: 0; line-height: 26px;
  }
  .line {
    display: flex; align-items: center; gap: 7px;
    font-size: 16.5px; color: var(--text-grey);
    margin: 2px 0 0; line-height: 24px;
  }
  .person + .person { margin-top: 19px; }
  .line svg { width: 13px; height: 13px; fill: var(--text-grey); }
  .registration { margin-top: 28px; }
  .registration .line { margin: 0 0 6px; }
  .registration strong { color: var(--brand-blue); font-weight: 700; }
  .email { margin-top: 14px; }
  .email svg { width: 15px; height: 11px; fill: var(--brand-blue); }

  .services {
    position: absolute; left: 348px; top: 242px;
    list-style: none; margin: 0; padding: 0;
  }
  .services li {
    display: flex; align-items: center; gap: 8px;
    font-size: 17px; color: var(--text-grey); line-height: 24px;
  }
  .services svg { width: 15px; height: 15px; }

  .band { position: absolute; bottom: 0; height: 26px; }
  .band--grey { left: 0; width: 335px; background: var(--brand-grey); }
  .band--blue { left: 342px; right: 0; background: var(--brand-blue); }
</style>
</head>
<body>
<div class="canvas">
  <section class="card card--front" aria-label="Card front">
    <h1 class="wordmark">Tarnwell<br>Roof Plumbing</h1>
  </section>

  <section class="card card--back" aria-label="Card back">
    <div class="contacts">
      <div class="person">
        <p class="person__name">Colin</p>
        <p class="line"><svg viewBox="0 0 24 24"><path d="M6.6 10.8a15.1 15.1 0 0 0 6.6 6.6l2.2-2.2a1 1 0 0 1 1-.25 11.4 11.4 0 0 0 3.6.57 1 1 0 0 1 1 1V20a1 1 0 0 1-1 1A17 17 0 0 1 3 4a1 1 0 0 1 1-1h3.5a1 1 0 0 1 1 1c0 1.25.2 2.45.57 3.57a1 1 0 0 1-.25 1z"/></svg>0468305172</p>
      </div>
      <div class="person">
        <p class="person__name">Finn</p>
        <p class="line"><svg viewBox="0 0 24 24"><path d="M6.6 10.8a15.1 15.1 0 0 0 6.6 6.6l2.2-2.2a1 1 0 0 1 1-.25 11.4 11.4 0 0 0 3.6.57 1 1 0 0 1 1 1V20a1 1 0 0 1-1 1A17 17 0 0 1 3 4a1 1 0 0 1 1-1h3.5a1 1 0 0 1 1 1c0 1.25.2 2.45.57 3.57a1 1 0 0 1-.25 1z"/></svg>0419587364</p>
      </div>
      <div class="registration">
        <p class="line"><strong>Lic #</strong> 614903K</p>
        <p class="line"><strong>ABN #</strong> 52716340951</p>
      </div>
      <p class="line email"><svg viewBox="0 0 20 14"><path d="M0 0h20v14H0z M1.5 1.5 10 8l8.5-6.5" stroke="#fff" stroke-width="1.3"/></svg>tr7win5@mailvane.com</p>
    </div>

    <p class="wordmark">Tarnwell<br>Roof Plumbing</p>

    <ul class="services">
      <li><svg viewBox="0 0 16 16"><rect x="1" y="2" width="12" height="12" fill="none" stroke="#0f52a0" stroke-width="1.8"/><path d="M4 7.5 7 10.5 15 2" fill="none" stroke="#0f52a0" stroke-width="2"/></svg>Metal Roofing</li>
      <li><svg viewBox="0 0 16 16"><rect x="1" y="2" width="12" height="12" fill="none" stroke="#0f52a0" stroke-width="1.8"/><path d="M4 7.5 7 10.5 15 2" fill="none" stroke="#0f52a0" stroke-width="2"/></svg>Fascia</li>
      <li><svg viewBox="0 0 16 16"><rect x="1" y="2" width="12" height="12" fill="none" stroke="#0f52a0" stroke-width="1.8"/><path d="M4 7.5 7 10.5 15 2" fill="none" stroke="#0f52a0" stroke-width="2"/></svg>Gutter</li>
      <li><svg viewBox="0 0 16 16"><rect x="1" y="2" width="12" height="12" fill="none" stroke="#0f52a0" stroke-width="1.8"/><path d="M4 7.5 7 10.5 15 2" fill="none" stroke="#0f52a0" stroke-width="2"/></svg>Edge Protection</li>
    </ul>

    <div class="band band--grey"></div>
    <div class="band band--blue"></div>
  </section>
</div>
</body>
</html>
```